Business Card Design for Animal Clinic

We are seeking a two sided business card design. The primary side should include our logo (provided in AI and EPS files) address, phone, website, and if possible "Follow Us" with icons for Facebook, Google+, and Twitter.

The back of the card needs to included space for appointment reminders.

Company Name:
Brackenfield Animal Clinic

Doctor Name:
To be provided to winner

Adress:
To be provided to winner

Phone:
to be provided to winner

Website:
www.brackenfieldanimalclinic.example

```html
<!DOCTYPE html>
<html lang="en">
<head>
<meta charset="utf-8">
<title>Brackenfield Animal Clinic – Business Card</title>
<link href="https://fonts.googleapis.com/css2?family=Play:wght@400;700&display=swap" rel="stylesheet">
<style>
  :root {
    --clinic-red: #a8322d;
    --ink: #4a4a4a;
    --rule: #cfcfcf;
    --card: #ffffff;
    --stage: #eeeae6;
    --faint: #f1e6e5;
  }
  * { margin: 0; padding: 0; box-sizing: border-box; }
  html, body { width: 1200px; height: 841px; overflow: hidden; }
  body {
    background: var(--stage);
    font-family: "Play", "Trebuchet MS", sans-serif;
    color: var(--ink);
    display: flex;
    align-items: center;
    justify-content: center;
    gap: 40px;
  }
  .card {
    position: relative;
    width: 560px;
    height: 320px;
    background: var(--card);
    box-shadow: 0 6px 20px rgba(0,0,0,0.14);
    overflow: hidden;
  }

  /* Front */
  .brand {
    position: absolute;
    left: 40px;
    top: 58px;
    display: flex;
    align-items: center;
    gap: 14px;
  }
  .brand-mark {
    width: 26px; height: 26px;
    border-radius: 50%;
    background: var(--clinic-red);
  }
  .brand-name {
    font-size: 25px;
    line-height: 1.15;
    color: var(--clinic-red);
    letter-spacing: 0.5px;
  }
  .divider {
    position: absolute;
    left: 300px; top: 104px;
    width: 1px; height: 112px;
    background: var(--rule);
  }
  .contact {
    position: absolute;
    left: 316px; top: 102px;
    font-size: 14px;
    line-height: 1.35;
  }
  .contact .person { color: var(--clinic-red); font-weight: 700; font-size: 15px; }
  .contact .role { margin-bottom: 10px; }
  .contact .phone { display: flex; align-items: center; gap: 6px; margin-top: 3px; }
  .follow { display: flex; align-items: center; gap: 4px; color: var(--clinic-red); font-weight: 700; margin-top: 2px; }
  .follow .social { width: 14px; height: 14px; background: var(--clinic-red); border-radius: 2px; }
  .follow .label { margin-right: 4px; }
  .swoosh { position: absolute; left: 0; bottom: 0; width: 560px; height: 120px; }
  .website-text {
    fill: #fff;
    font-family: "Play", "Trebuchet MS", sans-serif;
    font-size: 12.5px;
    letter-spacing: 2px;
  }

  /* Back */
  .appointment {
    position: absolute;
    left: 34px; top: 34px;
    font-size: 13px;
  }
  .appointment .intro { color: var(--clinic-red); margin-bottom: 10px; }
  .field { display: flex; align-items: flex-end; gap: 8px; color: var(--clinic-red); margin-bottom: 12px; }
  .field .fill { width: 150px; border-bottom: 1px dotted #999; height: 12px; }
  .back-brand {
    position: absolute;
    right: 34px; top: 32px;
    text-align: right;
    font-size: 21px;
    line-height: 1.15;
    color: var(--clinic-red);
  }
  .faint-mark {
    position: absolute;
    right: 60px; top: 130px;
    width: 100px; height: 100px;
    border-radius: 50%;
    background: var(--faint);
  }
  .policy {
    position: absolute;
    left: 0; right: 0; bottom: 36px;
    text-align: center;
  }
  .policy .title { color: var(--clinic-red); font-size: 15px; margin-bottom: 6px; }
  .policy .note { font-size: 14px; color: #3a3a3a; }
</style>
</head>
<body>

  <section class="card card-front" aria-label="Business card front">
    <div class="brand">
      <div class="brand-mark"></div>
      <div class="brand-name">Brackenfield<br>Animal Clinic</div>
    </div>

    <div class="divider"></div>

    <div class="contact">
      <div class="person">Your Name</div>
      <div class="role">President</div>
      <div>418 N. Larkmoor Road</div>
      <div>Fenwick Springs, FL 32990</div>
      <div class="phone">
        <svg width="11" height="13" viewBox="0 0 11 13" aria-hidden="true">
          <path d="M2 0.5 L4 0.5 L5 4 L3.5 5 C4.2 7 5.3 8.4 6.5 9.3 L7.8 8 L10.5 9.5 L10 12 C5 12.5 0.5 7 1 1.5 Z" fill="var(--clinic-red)"/>
        </svg>
        <span>(555) 014-2287</span>
      </div>
      <div class="follow">
        <span class="label">Follow Us:</span>
        <span class="social"></span><span class="social"></span><span class="social"></span>
      </div>
    </div>

    <svg class="swoosh" viewBox="0 0 560 120">
      <defs>
        <path id="website-path" d="M26 76 C150 72 290 88 470 122"/>
      </defs>
      <path d="M0 18 C180 8 380 50 560 120 L0 120 Z" fill="var(--clinic-red)"/>
      <path d="M0 30 C190 22 380 66 540 120" fill="none" stroke="#fff" stroke-width="3"/>
      <text class="website-text"><textPath href="#website-path">www.brackenfieldanimalclinic.example</textPath></text>
    </svg>
  </section>

  <section class="card card-back" aria-label="Business card back, appointment reminder">
    <div class="appointment">
      <div class="intro">You have an appointment:</div>
      <div class="field"><span>Pet's Name:</span><span class="fill"></span></div>
      <div class="field"><span>Date:</span><span class="fill"></span></div>
      <div class="field"><span>Time:</span><span class="fill"></span></div>
    </div>

    <div class="back-brand">Brackenfield<br>Animal Clinic</div>
    <div class="faint-mark"></div>

    <div class="policy">
      <div class="title">Cancelation Policy</div>
      <div class="note">24 HR notice required for cancelations (xxx) xxx-xxxx</div>
    </div>
  </section>

</body>
</html>
```